Daniel Fordyce Psychotherapy Business Card Design Project

I need a welcoming business card for a Somatic Psychotherapy private practice based in Melbourne, Australia. I help individual clients to work through issues in their life that are inhibiting achieving their full potential. I would like a san serif font and the oculars are:
blue: R:37 G:61 B:95 C:93 M:77 Y:38 K:28
orange: R:241 G:103 B:43 C:0 M:74 Y:93 K:0
The final design should communicate warm, welcoming and safe environment in which clients are supported to grow. It should also convey a collaborative approach to achieve success between me (the therapist) and the client. The uploaded file is my new logo. Also an organic look and feel while maintaining professionalism and a clean, simple look is sought after.
In addition to the logo my details are:
Daniel Fordyce
Psychotherapist
B.Arts., Grad Dip. T&D., Dip.Som.Psych, MRTOB, MFLENG
0417 552 908
dfordyce@danielfordyce.com.au
www.danielfordyce.com.au
Psychotherapy Clients
Environment

```html
<!DOCTYPE html>
<html lang="en">
<head>
<meta charset="utf-8">
<title>Daniel Fordyce Psychotherapy – Business Card</title>
<link rel="stylesheet" href="https://fonts.googleapis.com/css2?family=Montserrat:wght@400;500&family=Open+Sans:wght@400&display=swap">
<style>
  :root {
    --brand-blue: #253d5f;
    --brand-orange: #f1672b;
    --card-stock: #ededed;
    --band-grey: #d6d6d8;
    --backdrop: #2b2c2f;
  }
  * { margin: 0; padding: 0; box-sizing: border-box; }
  html, body { width: 1200px; height: 800px; overflow: hidden; }
  body {
    background: var(--backdrop);
    font-family: "Montserrat", sans-serif;
    color: var(--brand-blue);
    position: relative;
  }
  .card {
    position: absolute;
    top: 216px;
    width: 565px;
    height: 325px;
    background: var(--card-stock);
  }
  .card--front { left: 23px; }
  .card--back { left: 612px; }

  .brand {
    position: absolute;
    left: 0; right: 0;
    display: flex;
    align-items: center;
    justify-content: center;
    gap: 14px;
  }
  .card--front .brand { top: 122px; }
  .card--back .brand { top: 46px; }
  .brand__dot {
    width: 58px; height: 58px;
    border-radius: 50%;
    background: var(--brand-orange);
    flex: none;
  }
  .brand__name {
    font-weight: 500;
    font-size: 25px;
    line-height: 1.1;
    color: var(--brand-blue);
  }

  .credentials {
    position: absolute;
    left: 25px; right: 17px;
    top: 277px;
    height: 35px;
    border-radius: 18px;
    background: var(--band-grey);
    font-family: "Open Sans", sans-serif;
    font-size: 15px;
    color: var(--brand-blue);
    display: flex;
    align-items: center;
    justify-content: center;
  }

  .contact {
    position: absolute;
    left: 0; right: 0;
    top: 144px;
    text-align: center;
  }
  .contact__name { font-size: 22px; font-weight: 400; line-height: 1.2; }
  .contact__role { font-size: 15px; color: var(--brand-orange); margin-top: 2px; }
  .contact__rule {
    width: 86px; height: 2px;
    background: var(--brand-orange);
    margin: 9px auto 16px;
  }
  .contact__line {
    font-family: "Open Sans", sans-serif;
    font-size: 17px;
    line-height: 24px;
  }
</style>
</head>
<body>
  <section class="card card--front">
    <div class="brand">
      <span class="brand__dot"></span>
      <span class="brand__name">Daniel Fordyce<br>Psychotherapy</span>
    </div>
    <p class="credentials">B.Arts., Grad Dip. T&amp;D., Dip.Som.Psych, MRTOB, MFLENG</p>
  </section>

  <section class="card card--back">
    <div class="brand">
      <span class="brand__dot"></span>
      <span class="brand__name">Daniel Fordyce<br>Psychotherapy</span>
    </div>
    <div class="contact">
      <p class="contact__name">Daniel Fordyce</p>
      <p class="contact__role">Psychotherapist</p>
      <div class="contact__rule"></div>
      <p class="contact__line">0417 552 908</p>
      <p class="contact__line">dfordyce@danielfordyce.com.au</p>
      <p class="contact__line">www.danielfordyce.com.au</p>
    </div>
  </section>
</body>
</html>
```